Business Card Design Harbor of Calm

mental health provider
contemporary
warmth
inviting

Target Market(s)

mental health clients adults

Industry/Entity Type

Mental Health

Contact Information for Business Card

Danielle Arkwright PMHNP
2841 SW Tenley Ave
Suite 384C
Portland OR 97318
Fax 503-555-0182
Tel 503-555-0147
Email danielle@darkwright.example
Website darkwright.example

Requirements
Nice to have
• see above
Should not have
• no medical logos

```html
<!DOCTYPE html>
<html lang="en">
<head>
<meta charset="utf-8">
<title>Harbor of Calm – Business Card</title>
<link href="https://fonts.googleapis.com/css2?family=Oswald:wght@300;400;500&display=swap" rel="stylesheet">
<style>
  :root{
    --bg:#2b2b2b;
    --purple:#a13f9e;
    --purple-deep:#8a2789;
    --purple-light:#b556b2;
    --cream:#f4f2e6;
    --white:#ffffff;
    --ink:#1e1e1e;
    --ghost:#d2d2d2;
  }
  *{margin:0;padding:0;box-sizing:border-box}
  html,body{width:1200px;height:900px;overflow:hidden;background:var(--bg);font-family:'Oswald',sans-serif}
  .stage{position:relative;width:1200px;height:900px}
  .card{position:absolute;left:310px;width:580px;height:330px;overflow:hidden;box-shadow:0 10px 30px rgba(0,0,0,.5)}

  /* back */
  .card--back{top:75px;background:linear-gradient(160deg,var(--purple-light),var(--purple-deep))}
  .card--back .edge-tab{position:absolute;background:var(--white);width:54px;height:44px}
  .card--back .edge-tab--top{top:26px;right:0}
  .card--back .edge-tab--bottom{bottom:26px;left:0}
  .brand{position:absolute;left:0;right:0;top:140px;display:flex;justify-content:center;align-items:center;gap:14px}
  .brand__dot{width:22px;height:22px;border-radius:50%;background:var(--white)}
  .brand__name{color:var(--white);font-weight:300;font-size:44px;letter-spacing:1px}

  /* front */
  .card--front{top:480px;background:linear-gradient(180deg,var(--white),var(--cream))}
  .front__ghost-name{position:absolute;left:22px;top:6px;font-weight:300;font-size:72px;color:var(--ghost);white-space:nowrap;letter-spacing:1px}
  .front__band{position:absolute;left:270px;right:0;top:112px;height:40px;background:var(--purple);border-radius:12px 0 0 12px}
  .front__band svg{position:absolute;left:16px;top:8px}
  .front__tab{position:absolute;left:0;top:176px;width:52px;height:38px;background:var(--purple);border-radius:0 10px 10px 0}
  .front__tab svg{position:absolute;left:12px;top:9px}
  .holder{position:absolute;left:70px;top:160px;line-height:1}
  .holder__name{font-size:26px;font-weight:400;color:var(--ink)}
  .holder__first{color:var(--purple)}
  .holder__title{font-size:15px;font-weight:500;color:var(--ink);margin-top:4px;display:block}
  .contact{position:absolute;left:40px;top:222px;color:var(--ink);font-size:15px;font-weight:400}
  .contact__row{display:flex;align-items:center;gap:10px;height:30px}
  .contact__grid{display:grid;grid-template-columns:240px 220px;row-gap:0}
  .contact__row svg{flex:none}
</style>
</head>
<body>
<div class="stage">

  <section class="card card--back" aria-label="Card back">
    <div class="edge-tab edge-tab--top"></div>
    <div class="edge-tab edge-tab--bottom"></div>
    <div class="brand">
      <span class="brand__dot"></span>
      <span class="brand__name">Danielle Arkwright</span>
    </div>
  </section>

  <section class="card card--front" aria-label="Card front">
    <div class="front__ghost-name">Danielle Arkwright</div>

    <div class="front__band">
      <svg width="290" height="24" viewBox="0 0 290 24">
        <g fill="var(--white)">
          <polygon points="0,12 24,2 17,12 24,22" opacity=".35"/>
          <polygon points="50,12 74,2 67,12 74,22" opacity=".45"/>
          <polygon points="100,12 124,2 117,12 124,22" opacity=".55"/>
          <polygon points="150,12 174,2 167,12 174,22" opacity=".7"/>
          <polygon points="200,12 224,2 217,12 224,22" opacity=".85"/>
          <polygon points="250,12 274,2 267,12 274,22"/>
        </g>
      </svg>
    </div>

    <div class="front__tab">
      <svg width="24" height="20" viewBox="0 0 24 20"><polygon points="24,10 0,0 7,10 0,20" fill="var(--white)"/></svg>
    </div>

    <div class="holder">
      <span class="holder__name"><span class="holder__first">Danielle</span> Arkwright</span>
      <span class="holder__title">PMHNP</span>
    </div>

    <div class="contact">
      <div class="contact__row">
        <svg width="16" height="20" viewBox="0 0 16 20"><path d="M8 0a8 8 0 0 0-8 8c0 6 8 12 8 12s8-6 8-12a8 8 0 0 0-8-8zm0 11a3 3 0 1 1 0-6 3 3 0 0 1 0 6z" fill="var(--ink)"/></svg>
        <span>2841 SW Tenley Ave Suite 384C Portland OR 97318</span>
      </div>
      <div class="contact__grid">
        <div class="contact__row">
          <svg width="20" height="20" viewBox="0 0 20 20"><rect width="20" height="20" rx="4" fill="var(--ink)"/><path d="M6 4l2 3-1.3 1.3a8 8 0 0 0 5 5L13 12l3 2-1.5 2.5C9 16 4 11 3.5 5.5z" fill="var(--white)"/></svg>
          <span>503-555-0147</span>
        </div>
        <div class="contact__row">
          <svg width="22" height="20" viewBox="0 0 22 20"><rect x="1" y="6" width="20" height="13" rx="2" fill="none" stroke="var(--ink)" stroke-width="2"/><rect x="5" y="1" width="12" height="8" fill="var(--white)" stroke="var(--ink)" stroke-width="2"/><rect x="5" y="12" width="12" height="2" fill="var(--ink)"/></svg>
          <span>503-555-0182</span>
        </div>
        <div class="contact__row">
          <svg width="22" height="16" viewBox="0 0 22 16"><rect width="22" height="16" fill="var(--ink)"/><path d="M1 1l10 8 10-8" fill="none" stroke="var(--white)" stroke-width="1.5"/></svg>
          <span>danielle@darkwright.example</span>
        </div>
        <div class="contact__row">
          <svg width="18" height="18" viewBox="0 0 18 18"><g fill="none" stroke="var(--ink)" stroke-width="1.4"><circle cx="9" cy="9" r="8"/><ellipse cx="9" cy="9" rx="3.5" ry="8"/><path d="M1 9h16M2.5 5h13M2.5 13h13"/></g></svg>
          <span>darkwright.example</span>
        </div>
      </div>
    </div>
  </section>

</div>
</body>
</html>
```